mobile app - telecom industry

We are a tech/service company. Our product is a mobile application for physical site inspection called “Veko”. Our target industry is telecommunica...

Target Market(s)

telecommunication

Industry/Entity Type

Industry

Requirements
Must have
• Screen size Nimbus 5 - Android
• Suggest 3 colors
• Design 9 pages

```html
<!DOCTYPE html>
<html lang="en">
<head>
<meta charset="utf-8">
<title>Veko – Home</title>
<link rel="stylesheet" href="https://fonts.googleapis.com/css2?family=Montserrat:wght@700&family=Roboto:wght@400;500&display=swap">
<style>
  :root {
    --white: #ffffff;
    --ink: #1e1e1e;
    --tile: #3a3a3a;
    --tile-text: #ffffff;
    --stage: #efefef;
    --stage-deep: #e2e2e2;
    --nav-icon: #333333;
  }
  * { margin: 0; padding: 0; box-sizing: border-box; }
  html, body { width: 1200px; height: 2328px; overflow: hidden; background: var(--white); }
  .screen { position: relative; width: 1200px; height: 2328px; font-family: "Roboto", sans-serif; color: var(--ink); }

  .status-bar { position: absolute; top: 0; left: 0; right: 0; height: 136px; }
  .status-icons { position: absolute; right: 40px; top: 22px; display: flex; align-items: center; gap: 14px; }
  .status-time { font-size: 40px; font-weight: 500; }

  .app-header { position: absolute; top: 136px; left: 0; right: 0; height: 184px; }
  .back-button { position: absolute; left: 64px; top: 50px; }
  .app-title { position: absolute; left: 0; right: 0; top: 40px; text-align: center; font-family: "Montserrat", sans-serif; font-weight: 700; font-size: 78px; letter-spacing: 2px; }

  .stage { position: absolute; top: 320px; left: 0; right: 0; height: 1780px; background: var(--stage); }
  .stage-art { position: absolute; top: 0; right: 0; width: 560px; height: 1780px;
    background: radial-gradient(ellipse at 70% 45%, var(--stage-deep) 0%, var(--stage) 70%); }

  .tile { position: absolute; width: 448px; height: 360px; background: var(--tile); border-radius: 0 8px 8px 0; color: var(--tile-text); display: flex; flex-direction: column; align-items: center; }
  .tile svg { margin-top: 78px; }
  .tile-label { position: absolute; bottom: 54px; left: 0; right: 0; text-align: center; font-size: 44px; }
  .tile-open { top: 452px; left: 0; }
  .tile-close { top: 840px; left: 0; }
  .tile-sync { top: 1228px; left: 0; }
  .tile-create { top: 1616px; left: 0; }
  .tile-settings { top: 1616px; left: 836px; width: 364px; border-radius: 8px 0 0 8px; }

  .nav-bar { position: absolute; top: 2100px; left: 0; right: 0; height: 228px; background: var(--white); }
  .nav-bar svg { position: absolute; top: 82px; }
</style>
</head>
<body>
<div class="screen">
  <div class="status-bar">
    <div class="status-icons">
      <svg width="52" height="40" viewBox="0 0 52 40"><path d="M26 38 L2 10 A38 38 0 0 1 50 10 Z" fill="var(--ink)"/></svg>
      <svg width="40" height="40" viewBox="0 0 40 40"><path d="M38 2 V38 H2 Z" fill="var(--ink)"/></svg>
      <svg width="24" height="44" viewBox="0 0 24 44"><rect x="7" y="0" width="10" height="4" fill="var(--ink)"/><rect x="0" y="4" width="24" height="40" rx="2" fill="var(--ink)"/></svg>
      <span class="status-time">12:30</span>
    </div>
  </div>

  <header class="app-header">
    <svg class="back-button" width="48" height="84" viewBox="0 0 48 84"><path d="M42 6 L8 42 L42 78" fill="none" stroke="var(--ink)" stroke-width="9" stroke-linecap="round" stroke-linejoin="round"/></svg>
    <h1 class="app-title">VEKO</h1>
  </header>

  <main class="stage">
    <div class="stage-art" role="img" aria-label="Faint background illustration of a telecom tower"></div>
  </main>

  <div class="tile tile-open">
    <svg width="136" height="112" viewBox="0 0 136 112"><path d="M6 8 H50 L60 20 H130 V104 H6 Z M6 36 H130" fill="none" stroke="#fff" stroke-width="7" stroke-linejoin="round"/></svg>
    <span class="tile-label">Open WO</span>
  </div>
  <div class="tile tile-close">
    <svg width="120" height="120" viewBox="0 0 120 120"><path d="M10 10 L110 110 M110 10 L10 110" stroke="#fff" stroke-width="12" stroke-linecap="round"/></svg>
    <span class="tile-label">Close WO</span>
  </div>
  <div class="tile tile-sync">
    <svg width="128" height="128" viewBox="0 0 128 128" fill="none" stroke="#fff" stroke-width="12" stroke-linecap="round">
      <path d="M22 54 A44 44 0 0 1 102 38"/><path d="M106 74 A44 44 0 0 1 26 90"/>
      <path d="M104 14 V40 H78" stroke-linejoin="round"/><path d="M24 114 V88 H50" stroke-linejoin="round"/>
    </svg>
    <span class="tile-label">Synchronize</span>
  </div>
  <div class="tile tile-create">
    <svg width="132" height="132" viewBox="0 0 132 132" fill="none" stroke="#fff" stroke-width="8" stroke-linejoin="round">
      <path d="M70 16 H10 V122 H116 V62"/><path d="M110 8 L124 22 L66 80 L48 84 L52 66 Z"/>
    </svg>
    <span class="tile-label">Create New WO</span>
  </div>
  <div class="tile tile-settings">
    <svg width="128" height="128" viewBox="0 0 128 128">
      <g fill="#fff" transform="translate(64 64)">
        <rect x="-12" y="-60" width="24" height="28" rx="3"/>
        <rect x="-12" y="-60" width="24" height="28" rx="3" transform="rotate(45)"/>
        <rect x="-12" y="-60" width="24" height="28" rx="3" transform="rotate(90)"/>
        <rect x="-12" y="-60" width="24" height="28" rx="3" transform="rotate(135)"/>
        <rect x="-12" y="-60" width="24" height="28" rx="3" transform="rotate(180)"/>
        <rect x="-12" y="-60" width="24" height="28" rx="3" transform="rotate(225)"/>
        <rect x="-12" y="-60" width="24" height="28" rx="3" transform="rotate(270)"/>
        <rect x="-12" y="-60" width="24" height="28" rx="3" transform="rotate(315)"/>
        <circle r="40"/>
      </g>
      <circle cx="64" cy="64" r="16" fill="var(--tile)"/>
    </svg>
    <span class="tile-label">Settings</span>
  </div>

  <nav class="nav-bar">
    <svg style="left:104px" width="64" height="72" viewBox="0 0 64 72"><path d="M58 6 V66 L6 36 Z" fill="none" stroke="var(--nav-icon)" stroke-width="7" stroke-linejoin="round"/></svg>
    <svg style="left:562px" width="76" height="76" viewBox="0 0 76 76"><circle cx="38" cy="38" r="33" fill="none" stroke="var(--nav-icon)" stroke-width="7"/></svg>
    <svg style="left:1030px" width="68" height="68" viewBox="0 0 68 68"><rect x="4" y="4" width="60" height="60" fill="none" stroke="var(--nav-icon)" stroke-width="7"/></svg>
  </nav>
</div>
</body>
</html>
```